Bertucci Estates Wine flyer

We have imported 4 wines and need a brochure that talks about them as well as some info about the winery they come from.

Target Market(s)

Wine drinkers; young professionals

Colors
ec1f27
9bcb3c
3176b5
f78f20

Requirements
Must have
• Wine elements - vintage look
Should not have
• Clipart look

```html
<!DOCTYPE html>
<html lang="en">
<head>
<meta charset="utf-8">
<title>Bertucci Estates – Wine Brochure</title>
<link rel="stylesheet" href="https://fonts.googleapis.com/css2?family=Dancing+Script:wght@500;700&display=swap">
<style>
  :root {
    --backdrop: #d9c08f;
    --paper: #efdfb3;
    --paper-deep: #e2cb92;
    --ink: #3a2e22;
    --ink-soft: #7a6a4e;
    --wine: #a3161c;
    --wine-dark: #5a0d10;
    --wine-bright: #ec1f27;
    --ornament: #c9ad74;
    --skyline: #8d8a5c;
  }
  * { box-sizing: border-box; margin: 0; padding: 0; }
  html, body { width: 1200px; height: 1200px; overflow: hidden; }
  body {
    background: var(--backdrop);
    font-family: "Dancing Script", cursive;
    color: var(--ink);
    position: relative;
  }
  .ornament-band {
    position: absolute; left: 370px; width: 460px; height: 36px;
    background: linear-gradient(90deg, transparent, var(--ornament), transparent);
    opacity: .45; border-radius: 18px;
  }
  .ornament-band.top { top: 22px; }
  .ornament-band.bottom { bottom: 22px; }

  .brochure {
    position: absolute; left: 60px; top: 150px;
    width: 1080px; height: 900px;
    display: flex; gap: 0;
    box-shadow: 0 6px 24px rgba(80, 55, 20, .25);
  }
  .panel {
    position: relative; flex: 1;
    background: radial-gradient(ellipse at 40% 35%, var(--paper) 0%, var(--paper) 55%, var(--paper-deep) 100%);
    border-right: 1px solid rgba(120, 90, 40, .18);
    overflow: hidden;
  }
  .panel:last-child { border-right: none; }

  /* Cover panel */
  .brand {
    position: absolute; top: 90px; left: 40px;
    display: flex; align-items: center; gap: 12px;
  }
  .brand-mark {
    width: 22px; height: 22px; background: var(--wine-dark);
  }
  .brand-name {
    font-size: 36px; font-weight: 700; color: var(--ink);
  }
  .wine-pour {
    position: absolute; top: 250px; left: 0; width: 360px; height: 340px;
    background: radial-gradient(ellipse at 65% 55%, var(--wine) 0%, var(--wine-dark) 45%, rgba(163,22,28,.15) 70%, transparent 78%);
  }
  .skyline {
    position: absolute; bottom: 0; left: 0; width: 100%; height: 200px;
    background: linear-gradient(180deg, transparent 0%, rgba(141,138,92,.45) 45%, var(--skyline) 100%);
  }

  /* Text panels */
  .copy {
    padding: 70px 40px 0;
    font-size: 23px; line-height: 1.32; color: var(--ink);
  }
  .copy p + p { margin-top: 22px; }
  .copy.light { color: var(--ink-soft); font-size: 20px; }
  .bottle-sketch {
    position: absolute; bottom: 60px; right: 40px; width: 120px; height: 230px;
    background: linear-gradient(180deg, transparent, rgba(168,146,96,.55));
    border-radius: 40px 40px 8px 8px;
  }
</style>
</head>
<body>
  <div class="ornament-band top" role="img" aria-label="Faint vintage scrollwork ornament"></div>

  <main class="brochure">
    <section class="panel panel-cover">
      <div class="brand">
        <span class="brand-mark"></span>
        <span class="brand-name">Bertucci Estates</span>
      </div>
      <div class="wine-pour" role="img" aria-label="Red wine pouring and splashing into a tilted glass"></div>
      <div class="skyline" role="img" aria-label="Sepia sketch of an old Italian hill town"></div>
    </section>

    <section class="panel panel-story">
      <div class="copy">
        <p>Our cellar is modern and equipped with every latest technology in order to comply at all stages of production with the materia prima. Thanks to the passion of Vigneti Bertucci, they have avoided harsh techniques that inevitably lead to the loss of the character of the grapes.</p>
        <p>We produce some 90,000 bottles, making it possible for careful vineyard management to follow every detail. This care makes the highest quality with minimal impact of the land, a balance that allows us over time to grow.</p>
        <p>Our wines are among Italy's highest rated and now imported into the United States by our family.</p>
      </div>
    </section>

    <section class="panel panel-wines">
      <div class="copy light">
        <p>Each wine is made from grapes chilled by the sea breeze and sun to create an exceptional and balanced taste.</p>
        <p>Four labels, one family, and a coastline that gives every bottle its own voice.</p>
      </div>
      <div class="bottle-sketch" role="img" aria-label="Faint sketch of a wine bottle and glass"></div>
    </section>
  </main>

  <div class="ornament-band bottom" role="img" aria-label="Faint vintage scrollwork ornament"></div>
</body>
</html>
```